Lumera Ostvik

I need you to design me a business card, with the same logo you did for my company.
It has to include this information.
Thx.
Contact details and other information I suppose it would be better if they were on the back of the card.
Company Name: LumeraOstvik
Commercial Name: Tomás Ibarra Quesada
Company activity: Cosmetics Distribution
Contact email: support@lumeost.com
Contact email: comercial@lumeost.com
Company website: https: //lumeost.com/
Company phone: +376 418 292
Instagram https://www.instagram.com/lumeraostvik/

```html
<!DOCTYPE html>
<html lang="en">
<head>
<meta charset="utf-8">
<title>Lumera Ostvik — Business Card</title>
<link rel="stylesheet" href="https://fonts.googleapis.com/css2?family=Montserrat:wght@400;600&display=swap">
<style>
  :root {
    --bg: #e4e3e1;
    --paper: #ffffff;
    --magenta: #d1219a;
    --magenta-deep: #c4168c;
    --blush: #f4b6cc;
    --ink: #6b6b6b;
  }
  * { box-sizing: border-box; margin: 0; padding: 0; }
  html, body { width: 1200px; height: 801px; overflow: hidden; }
  body {
    background: var(--bg);
    font-family: "Montserrat", sans-serif;
    position: relative;
  }
  .card {
    position: absolute;
    top: 246px;
    width: 540px;
    height: 309px;
    box-shadow: 0 6px 18px rgba(0,0,0,0.12);
  }
  .card--details { left: 40px; background: var(--paper); }
  .card--brand {
    left: 620px;
    background: linear-gradient(160deg, var(--magenta) 0%, var(--magenta-deep) 100%);
  }

  /* Details side */
  .brand-block {
    position: absolute;
    left: 40px;
    top: 0;
    width: 210px;
    height: 100%;
    display: flex;
    flex-direction: column;
    align-items: center;
    justify-content: center;
    gap: 14px;
  }
  .brand-mark {
    width: 92px;
    height: 92px;
    border-radius: 50%;
    background: var(--blush);
  }
  .brand-name {
    font-weight: 600;
    font-size: 22px;
    color: var(--magenta);
    letter-spacing: 0.5px;
  }
  .divider {
    position: absolute;
    left: 270px;
    top: 54px;
    width: 1.5px;
    height: 200px;
    background: var(--magenta);
  }
  .contact-block {
    position: absolute;
    left: 292px;
    top: 62px;
    right: 20px;
  }
  .person-name {
    font-weight: 600;
    font-size: 17px;
    color: var(--magenta);
  }
  .person-role {
    font-size: 13px;
    color: var(--ink);
    margin-top: 3px;
    margin-bottom: 16px;
  }
  .contact-list { list-style: none; }
  .contact-item {
    display: flex;
    align-items: center;
    gap: 8px;
    font-size: 12.5px;
    color: var(--ink);
    line-height: 1;
    margin-bottom: 8px;
  }
  .contact-icon { width: 14px; height: 14px; flex: none; }

  /* Brand side */
  .brand-face {
    position: absolute;
    inset: 0;
    display: flex;
    flex-direction: column;
    align-items: center;
    justify-content: center;
    gap: 20px;
  }
  .brand-face .brand-mark {
    width: 130px;
    height: 130px;
    background: var(--paper);
  }
  .brand-face .brand-name {
    color: var(--paper);
    font-size: 34px;
  }
</style>
</head>
<body>

<section class="card card--details">
  <div class="brand-block">
    <div class="brand-mark" aria-hidden="true"></div>
    <div class="brand-name">Lumera Ostvik</div>
  </div>

  <div class="divider"></div>

  <div class="contact-block">
    <div class="person-name">Tomás Ibarra Quesada</div>
    <div class="person-role">Cosmetics Distribution</div>
    <ul class="contact-list">
      <li class="contact-item">
        <svg class="contact-icon" viewBox="0 0 24 24"><path fill="var(--magenta)" d="M6.6 10.8a15 15 0 0 0 6.6 6.6l2.2-2.2a1 1 0 0 1 1-.25 11.4 11.4 0 0 0 3.6.57 1 1 0 0 1 1 1V20a1 1 0 0 1-1 1A17 17 0 0 1 3 4a1 1 0 0 1 1-1h3.5a1 1 0 0 1 1 1c0 1.25.2 2.45.57 3.57a1 1 0 0 1-.25 1z"/></svg>
        +376 418 292
      </li>
      <li class="contact-item">
        <svg class="contact-icon" viewBox="0 0 24 24"><rect x="2" y="5" width="20" height="14" rx="1" fill="var(--magenta)"/><path d="M3 6l9 7 9-7" fill="none" stroke="#fff" stroke-width="1.6"/></svg>
        support@lumeost.com
      </li>
      <li class="contact-item">
        <svg class="contact-icon" viewBox="0 0 24 24"><rect x="2.5" y="5.5" width="19" height="13" rx="1" fill="none" stroke="var(--magenta)" stroke-width="1.6"/><path d="M3 6l9 7 9-7" fill="none" stroke="var(--magenta)" stroke-width="1.6"/></svg>
        comercial@lumeost.com
      </li>
      <li class="contact-item">
        <svg class="contact-icon" viewBox="0 0 24 24"><circle cx="12" cy="12" r="10" fill="var(--magenta)"/></svg>
        lumeraostvik
      </li>
      <li class="contact-item">
        <svg class="contact-icon" viewBox="0 0 24 24"><g fill="none" stroke="var(--magenta)" stroke-width="1.6"><circle cx="12" cy="12" r="9.5"/><ellipse cx="12" cy="12" rx="4" ry="9.5"/><path d="M2.5 12h19"/></g></svg>
        www.lumeost.com
      </li>
    </ul>
  </div>
</section>

<section class="card card--brand">
  <div class="brand-face">
    <div class="brand-mark" aria-hidden="true"></div>
    <div class="brand-name">Lumera Ostvik</div>
  </div>
</section>

</body>
</html>
```